"Brindle Oak Accupuncture" needs a Promotional Card - A6 size

Requirements
Must have
• Bright colours, pictures of happy people, acupuncture-related pictures.

```html
<!DOCTYPE html>
<html lang="en">
<head>
<meta charset="utf-8">
<title>Brindle Oak Accupuncture – Promotional Card</title>
<link href="https://fonts.googleapis.com/css2?family=Exo+2:ital,wght@0,400;0,600;1,400;1,600&family=Open+Sans:wght@400;600&family=Poppins:wght@700&display=swap" rel="stylesheet">
<style>
  :root{
    --bg:#f1f1f1;
    --teal:#4fd6cf;
    --cyan:#41e3e0;
    --coral:#f06552;
    --yellow:#f6e57e;
    --green:#a6dc7a;
    --white:#ffffff;
    --ink:#2a2424;
  }
  *{box-sizing:border-box;margin:0;padding:0}
  html,body{width:1200px;height:459px;overflow:hidden;background:var(--bg)}
  .stage{position:relative;width:1200px;height:459px}
  .card{position:absolute;top:46px;width:528px;height:367px;overflow:hidden}

  /* front */
  .card--front{left:45px;background:var(--teal)}
  .front__art{position:absolute;inset:0}
  .brand{position:absolute;left:14px;top:52px;width:160px;
    font-family:"Poppins",sans-serif;font-weight:700;font-size:22px;line-height:24px;color:var(--coral);text-align:center}
  .brand__dot{display:block;width:18px;height:18px;border-radius:50%;background:var(--coral);margin:0 auto 7px}
  .headline{position:absolute;left:248px;top:40px;color:var(--white);font-family:"Exo 2",sans-serif;font-style:italic;font-weight:400;white-space:nowrap}
  .headline__find{font-size:44px;line-height:48px}
  .headline__your{font-size:20px;letter-spacing:5px;margin-left:4px}
  .headline__balance{display:block;font-size:48px;font-weight:600;line-height:50px;margin-left:22px;letter-spacing:1px}
  .tagline{position:absolute;left:236px;top:272px;width:270px;color:var(--white);font-family:"Exo 2",sans-serif;text-align:center;white-space:nowrap}
  .tagline__kicker{font-size:11px;letter-spacing:2px}
  .tagline__main{font-size:20px;line-height:26px}
  .website{position:absolute;left:0;bottom:14px;width:400px;text-align:center;
    font-family:"Open Sans",sans-serif;font-weight:600;font-size:14px;letter-spacing:2px;color:var(--white)}

  /* back */
  .card--back{left:628px;background:var(--coral)}
  .back__photo{position:absolute;left:18px;top:0;width:131px;height:367px;
    background:radial-gradient(circle at 20% 60%,#8a8a8a 0,#3a3a3a 30%,#050505 60%)}
  .back__content{position:absolute;left:160px;top:20px;width:352px;font-family:"Open Sans",sans-serif;color:var(--ink)}
  .heading{font-family:"Exo 2",sans-serif;font-style:italic;font-weight:400;line-height:1}
  .heading__lead{display:block;color:var(--white);font-size:19px;margin-left:36px}
  .heading__main{display:block;color:var(--cyan);font-size:28px;font-weight:600;margin:2px 0 6px 36px}
  .heading--inline{font-size:23px;color:var(--white);margin:10px 0 4px 36px}
  .heading--inline strong{color:var(--cyan);font-weight:600}
  .copy{font-size:10.2px;line-height:13.4px}
  .benefits{list-style:none;margin:2px 0 0 36px;font-size:10.5px;line-height:14.2px}
  .benefits li{position:relative;padding-left:16px}
  .benefits li::before{content:"";position:absolute;left:0;top:3px;width:8px;height:8px;border-radius:50%;background:var(--white)}
  .practitioner{position:absolute;left:398px;top:248px;width:114px;height:114px;border-radius:50%;
    border:5px solid var(--cyan);background:linear-gradient(160deg,#d9d9d9,#5c5c5c)}
  .practitioner__name{position:absolute;left:404px;top:332px;padding:2px 10px;background:var(--cyan);
    font-family:"Open Sans",sans-serif;font-size:9px;color:var(--ink);border-radius:2px}
  .contact{position:absolute;left:160px;top:344px;width:230px;border-top:1px solid rgba(0,0,0,.35);padding-top:5px;
    display:flex;justify-content:space-between;font-family:"Open Sans",sans-serif;font-size:8.5px;color:var(--ink)}
  .contact b{font-weight:600}
</style>
</head>
<body>
<div class="stage">

  <section class="card card--front">
    <svg class="front__art" width="528" height="367" viewBox="0 0 528 367">
      <defs>
        <linearGradient id="handTone" x1="0" y1="0" x2="1" y2="1">
          <stop offset="0" stop-color="#f6d3a6" stop-opacity=".95"/>
          <stop offset="1" stop-color="#e7b381" stop-opacity=".6"/>
        </linearGradient>
        <linearGradient id="backTone" x1="0" y1="0" x2="1" y2="0">
          <stop offset="0" stop-color="#bfe9e6" stop-opacity="0"/>
          <stop offset="1" stop-color="#e8f6f3" stop-opacity=".8"/>
        </linearGradient>
      </defs>
      <circle cx="110" cy="240" r="160" fill="var(--yellow)"/>
      <circle cx="268" cy="232" r="140" fill="var(--green)" opacity=".85"/>
      <rect x="170" y="215" width="358" height="105" fill="url(#backTone)" role="img" aria-label="Photo of acupuncture needles placed along a patient's back"/>
      <path d="M0 190 Q120 210 200 300 L200 367 L0 367 Z" fill="url(#handTone)" role="img" aria-label="Photo of a practitioner's hand inserting an acupuncture needle"/>
      <circle cx="92" cy="48" r="136" fill="var(--white)"/>
      <path d="M0 330 Q260 300 528 320 L528 367 L0 367 Z" fill="var(--coral)"/>
    </svg>
    <div class="brand"><span class="brand__dot"></span>brindle oak accupuncture</div>
    <h1 class="headline"><span class="headline__find">find</span><span class="headline__your">your</span><span class="headline__balance">Balance</span></h1>
    <div class="tagline"><p class="tagline__kicker">ACUPUNCTURE THERAPY</p><p class="tagline__main">improve your well-being</p></div>
    <p class="website">www.brindleoak.com</p>
  </section>

  <section class="card card--back">
    <div class="back__photo" role="img" aria-label="Black and white photo of acupuncture needles in a shoulder"></div>
    <div class="back__content">
      <h2 class="heading"><span class="heading__lead">what is</span><span class="heading__main">acupuncture therapy?</span></h2>
      <p class="copy">Acupuncture is a component of the health care system of China that can be traced back at least 2,500 years. The general theory of acupuncture is based on the premise that there are patterns of energy flow (Qi) through the body that are essential for health. Disruptions of this flow are believed to be responsible for disease.</p>
      <h2 class="heading heading--inline">acupuncture <strong>benefits</strong></h2>
      <p class="copy">There is an ample amount of research that confirms certain health benefits:</p>
      <ul class="benefits">
        <li>Chronic Pain</li>
        <li>Arthritis</li>
        <li>Migraines, Headaches, and Neck</li>
        <li>Nausea and vomiting</li>
        <li>Anxiety</li>
        <li>Insomnia</li>
        <li>Heartburn &amp; Indigestion Pain</li>
      </ul>
    </div>
    <div class="practitioner" role="img" aria-label="Portrait photo of the practitioner"></div>
    <span class="practitioner__name">Dr. Elin Marsh</span>
    <div class="contact"><span><b>phone:</b> 555.210.348</span><span><b>street address</b> 48 Harrow Ln, UK</span></div>
  </section>

</div>
</body>
</html>
```